Oral Surgery Office Referral Form and Stationary designs.

Hi, I am a dentist/oral surgeon recently graduated and starting my own practice. Need help in designing an attractive, warm, appealing and Professional referral form (double sided), and stationary design. These will be used for Thank you notes, Professional letters, Front of a presentation folder, Notepads, envelopes, promotional products, Fax, etc... I do have a sample of a typical referral form and also have a logo as well as business card design that I will provide as a base to use. I will attach the files to this posting. Please, do some investigating on the Oral surgery / dental specialist websites as to some of the examples of the referral forms. Thanks and feel free to respond with any questions. Look forward to the designs - having the business card designed here was a great experience.
I will attach more files to clarify / show examples.

HELLO ALL,

I JUST WENT THROUGH THE BRIEF AND REALISED THAT THERE IS A MISTAKE IN MY POSTING. 
THE WEBSITE ADDRESS SHOULD READ:
 WWW.KRELDAX.COM 
IN MY ORIGINAL POSTING IT WAS MISSING THE "M".

TRULY APOLOGIZE FOR ANY INCONVENIENCE.
THANK YOU,
GERALD

Target Market(s)

Dental Professionals and oral surgery patients.

Industry/Entity Type

Dental

Requirements
Must have
• Has to have pictures of the mouth / teeth numbers/ map with directions. Needs to be warm and appealing. If possible to have it in a format that can be easily converted to a clickable one online. Don't know if possible. Thanks.
Should not have
• Typical dental designs .

```html
<!DOCTYPE html>
<html lang="en">
<head>
<meta charset="utf-8">
<title>Harbor Crest Oral Surgery – Patient Instructions</title>
<link href="https://fonts.googleapis.com/css2?family=Open+Sans:wght@400;700&display=swap" rel="stylesheet">
<style>
  :root {
    --teal: #1f8fa4;
    --ink: #111;
    --brown: #5b4a42;
    --grey: #555;
    --map: #e9ecee;
    --map-edge: #9aa3a8;
    --paper: #fff;
  }
  html, body { margin: 0; padding: 0; overflow: hidden; background: var(--paper); }
  .card {
    position: relative; width: 1200px; height: 775px; overflow: hidden;
    background: var(--paper); font-family: "Open Sans", Arial, sans-serif; color: var(--ink);
  }
  .abs { position: absolute; margin: 0; }
  .col { left: 40px; width: 380px; text-align: center; }

  .brand { top: 96px; display: flex; align-items: center; justify-content: center; gap: 10px; }
  .brand-dot { width: 18px; height: 18px; border-radius: 50%; background: var(--teal); flex: none; }
  .brand-name { color: var(--teal); font-size: 23px; font-weight: 400; line-height: 30px; }

  .doctor { top: 164px; color: var(--brown); font-weight: 700; font-size: 18px; line-height: 26px; }
  .board { top: 203px; color: var(--grey); font-size: 14px; line-height: 23px; }
  .phone { top: 266px; font-size: 20px; line-height: 27px; }
  .phone .fax { font-size: 17px; }

  .map { left: 43px; top: 343px; width: 364px; height: 215px; border: 2px solid var(--map-edge); box-sizing: border-box;
    background: linear-gradient(160deg, #f3f5f6, var(--map)); }
  .address { left: 33px; top: 565px; font-size: 24px; line-height: 31px; }

  .right { left: 430px; width: 790px; text-align: center; }
  .notice { top: 28px; font-size: 18px; line-height: 25.5px; }
  .assist { top: 140px; font-size: 20px; line-height: 24px; }
  .docs { top: 195px; font-size: 20px; line-height: 30px; }
  .heading { top: 279px; font-weight: 700; font-size: 19px; line-height: 25px; }

  .steps { left: 454px; top: 341px; width: 720px; padding: 0; list-style: none; }
  .steps li { position: relative; padding-left: 75px; font-size: 15.5px; line-height: 25px; }
  .steps li::before { content: ""; position: absolute; left: 0; top: 6px; width: 34px; height: 34px; background: var(--teal); }
  .steps li:nth-child(1) { margin-bottom: 8px; }
  .steps li:nth-child(2) { margin-bottom: 16px; }
  .steps li:nth-child(3) { margin-bottom: 15px; }
  .steps .cap { text-transform: uppercase; }

  .band { left: 0; top: 0; }
  .site { left: 84px; top: 720px; color: var(--paper); font-size: 23px; letter-spacing: 2px; }
</style>
</head>
<body>
<div class="card">
  <svg class="abs band" width="1200" height="775" viewBox="0 0 1200 775" aria-hidden="true">
    <path d="M0 688 C 400 668, 800 700, 1200 672 L1200 775 L0 775Z" fill="var(--teal)"/>
  </svg>

  <div class="abs col brand">
    <span class="brand-dot"></span>
    <span class="brand-name">Harbor Crest Oral Surgery</span>
  </div>
  <p class="abs col doctor">Gerald I. Varnell DDS, MD</p>
  <p class="abs col board">Diplomate, American Board of<br>Oral and Maxillofacial Surgeons</p>
  <p class="abs col phone">Tel (555) 317 0142<br><span class="fax">Fax (555) 317 0143</span></p>
  <div class="abs map" role="img" aria-label="Street map showing the office location near the main road"></div>
  <p class="abs address">2280 Linden Street<br>Riverton, NE 68190</p>

  <p class="abs right notice">PLEASE NOTE THAT IN MOST INSTANCES THE PATIENT IS FIRST SEEN FOR<br>CONSULATION TO REVIEW THE HEALTH HISTORY, DECIDE ON THE MOST<br>APPROPRIATE ANATHESIA AND&nbsp; TREATMENT PLAN<br>AND SCHEDULE A SEPARATE APPOINTMENT.</p>
  <p class="abs right assist">Please assist us by having the following information available<br>with you at the time of appointment</p>
  <p class="abs right docs">Your surgical referral slip and any xrays if applicable,<br>a list of medications, and insurance policy information</p>
  <p class="abs right heading">SPECIAL INSTRUCTIONS FOR PATIENTS HAVING<br>I.V. SEDATION / GENERAL ANESTHESIA</p>
  <ul class="abs steps">
    <li><span class="cap">No food or drink (including water) at least 6 hours prior to<br>your surgery unless otherwise indicated by the surgeon.</span><br>Some medicaitons may be continued and this will be discussed at your<br>consulation.</li>
    <li>A responsible adult must accompany you and REMAIN in the office<br>during the entire treatment. YOU cannot drive until the next day.<br>They must also be able to drive you home.</li>
    <li>Eat a light and easily digestible meal the night before the procedure.<br>Do not drink any alcoholic beverages the night before</li>
    <li>Wear comfortable clothing with sleeves which are easy to push up.</li>
  </ul>

  <p class="abs site">www.kreldax.com</p>
</div>
</body>
</html>
```